Personal Home Page

I'm an independent film maker that recently graduated with a master's in film making, I have done many short films and won awards, I have worked on many other film projects.
I like to have a single home page that's interactive, think crazy, funny, weired is very much welcome (rex moldan kinda) the sole purpose of this page is to promote myself and what I do very briefly with contact details, in a way if anyone goes to the site gets drown in and has fun viewing or experiencing it ! I love the magic designers bring to the table, I'm very open for any creative inputs, thanks
Here are just some examples of what I mean by interactive or entertaining :
http://www.pebrowave.com.sg/
http://www.vorticalon.com/
Reason: the designs submitted didn't meet the requirements in the brief
Target Market(s)
movie lovers, younger generation, art lovers, media production proffesionals
Requirements
Must have
- contact details, just an email would be enough !
Nice to have
- things relate to movie making, camera, film rolling...etc. but it's not a must
Should not have
- adult material, frightening elements (sudden loud scream or so)
A template that I can get for free online or build on qadu.com

```html
<!DOCTYPE html>
<html lang="en">
<head>
<meta charset="utf-8">
<title>Noel Avery – Film Maker</title>
<link href="https://fonts.googleapis.com/css2?family=Cinzel:wght@400;600;700&family=Arimo:wght@400&display=swap" rel="stylesheet">
<style>
:root{
  --paper:#ede6db;
  --paper-dark:#e2d8c9;
  --maroon:#6e0d0f;
  --maroon-dark:#560a0b;
  --teal:#6aa9a5;
  --teal-dark:#4f8c88;
  --ink:#2e2a27;
  --ink-soft:#4a4440;
  --grey:#6b6865;
  --footer:#d9cbb8;
  --white:#ffffff;
}
*{margin:0;padding:0;box-sizing:border-box}
html,body{width:1200px;height:900px;overflow:hidden}
body{background:radial-gradient(ellipse at 40% 40%,#f3eee6 0%,var(--paper) 55%,var(--paper-dark) 100%);font-family:"Arimo",Arial,sans-serif;color:var(--ink);position:relative}
.abs{position:absolute}
.festival-badge{left:201px;top:34px;width:309px;height:107px}
.cinema-art{left:582px;top:0;width:437px;height:212px;background:linear-gradient(180deg,#e6ddd0 0%,#d9cfc0 60%,rgba(237,230,219,0) 100%);opacity:.9}
.main-nav{left:181px;top:210px;width:842px;height:44px;background:var(--maroon);clip-path:polygon(0 4%,12% 2%,25% 6%,40% 0,55% 5%,70% 2%,85% 6%,98% 0,100% 8%,100% 100%,1% 100%,1% 90%,0 88%);display:flex;align-items:center;padding-left:15px}
.main-nav a{font-family:"Cinzel",serif;color:var(--white);text-decoration:none;font-size:13.5px;letter-spacing:.3px}
.main-nav a:nth-child(1){width:78px}
.main-nav a:nth-child(2){width:122px}
.main-nav a:nth-child(3){width:125px}
.main-nav a:nth-child(4){width:128px}
.main-nav a:nth-child(5){width:136px}
.video-panel{left:196px;top:300px;width:258px;height:235px;background:linear-gradient(160deg,#3f5430 0%,#22301c 40%,#141814 65%,#33393d 100%);box-shadow:3px 4px 6px rgba(0,0,0,.35)}
.play-btn{position:absolute;left:107px;top:95px}
.intro h1{position:absolute;left:474px;top:302px;font-family:"Cinzel",serif;font-weight:600;font-size:24px;color:var(--maroon);white-space:nowrap;letter-spacing:.3px}
.intro h2{position:absolute;left:474px;top:344px;font-family:"Cinzel",serif;font-weight:400;font-size:18px;color:var(--ink)}
.intro p{position:absolute;left:474px;top:385px;width:545px;font-size:10.6px;line-height:14.1px;color:var(--ink-soft)}
.more-btn{left:474px;top:490px;width:123px;height:31px;background:var(--maroon);color:var(--white);font-family:"Cinzel",serif;font-size:16px;display:flex;align-items:center;justify-content:center;text-decoration:none;clip-path:polygon(0 6%,30% 0,55% 8%,80% 0,100% 4%,100% 100%,0 100%)}
.awards-label{left:701px;top:488px;font-family:"Cinzel",serif;font-size:13px;color:var(--ink-soft);letter-spacing:.5px}
.award{top:513px;width:62px;height:62px;border:2px solid var(--grey);border-radius:50%}
.ribbon{height:40px;background:linear-gradient(180deg,#86bcb8,var(--teal) 60%,var(--teal-dark));clip-path:polygon(0 0,6% 10%,94% 10%,100% 0,97% 55%,100% 100%,94% 85%,6% 85%,0 100%,3% 55%);display:flex;align-items:center;justify-content:center;font-family:"Cinzel",serif;font-weight:700;font-style:italic;font-size:19px;color:#203735}
.card{background:var(--white);box-shadow:0 1px 3px rgba(0,0,0,.08)}
.what-ribbon{left:253px;top:610px;width:304px}
.what-card{left:268px;top:643px;width:274px;height:131px;padding:22px 22px 0 26px;font-size:10.6px;line-height:14.1px;color:var(--ink)}
.contact-ribbon{left:648px;top:610px;width:305px}
.contact-card{left:663px;top:643px;width:274px;height:131px;padding:17px 0 0 27px}
.contact-list{list-style:none;font-size:10.6px;color:var(--ink-soft)}
.contact-list li{position:relative;padding-left:23px;height:23px;line-height:14px}
.contact-list svg{position:absolute;left:0;top:1px}
.site-footer{left:0;top:826px;width:1200px;height:74px;background:var(--footer);border-top:1px solid #cbbca6}
.copyright{position:absolute;left:205px;top:34px;font-size:11px;color:var(--ink)}
.footer-nav{position:absolute;left:589px;top:34px;font-size:11px;color:var(--ink)}
.footer-nav a{color:var(--ink);text-decoration:none}
.footer-nav .sep{margin:0 9px}
</style>
</head>
<body>

<svg class="abs festival-badge" role="img" aria-label="Festival selection badge" viewBox="0 0 309 107">
  <rect x="20" y="8" width="269" height="91" rx="45" fill="none" stroke="#6e0d0f" stroke-width="3"/>
</svg>

<div class="abs cinema-art" role="img" aria-label="Pencil sketch of an empty cinema hall with rows of seats facing a screen"></div>

<nav class="abs main-nav">
  <a href="#">Home</a><a href="#">Film Making</a><a href="#">Short Films</a><a href="#">Won Awards</a><a href="#">Film Projects</a><a href="#">Contact Us</a>
</nav>

<div class="abs video-panel" role="img" aria-label="Video still of tropical plants beside a river, framed as a strip of film">
  <svg class="play-btn" width="44" height="44" viewBox="0 0 44 44"><circle cx="22" cy="22" r="19" fill="rgba(0,0,0,.15)" stroke="#f4f0ea" stroke-width="3"/><polygon points="17,13 31,22 17,31" fill="#f4f0ea"/></svg>
</div>

<section class="intro">
  <h1>I am Noel Avery. I do film making</h1>
  <h2>Watch this video!</h2>
  <p>Lorem Ipsum is simply dummy text of the printing and typesetting industry. Lorem Ipsum has been the industry's standard dummy text ever since the 1500s, when an unknown printer took a galley of type and scrambled it to make a type specimen book. It has survived not only five centuries, but also the leap into electronic typesetting, remaining essentially unchanged. It was popularised in the 1960s with the release of Letraset sheets containing Lorem Ipsum passages, and more recently with desktop publishing software like Aldus PageMaker including versions of Lorem Ipsum.</p>
</section>

<a class="abs more-btn" href="#">More Info</a>

<div class="abs awards-label">Won Awards:</div>
<div class="abs award" style="left:695px" role="img" aria-label="Award badge"></div>
<div class="abs award" style="left:790px" role="img" aria-label="Award badge"></div>
<div class="abs award" style="left:888px" role="img" aria-label="Award badge"></div>

<div class="abs ribbon what-ribbon">What I do</div>
<div class="abs card what-card">Lorem Ipsum is simply dummy text of the printing and typesetting industry. Lorem Ipsum has been the industry's standard dummy text ever since the 1500s, when an unknown printer took a galley of type and scrambled it to make a type specimen book.</div>

<div class="abs ribbon contact-ribbon">Cantact us</div>
<div class="abs card contact-card">
  <ul class="contact-list">
    <li><svg width="14" height="11" viewBox="0 0 14 11"><rect x="0.5" y="0.5" width="13" height="10" fill="none" stroke="#6aa9a5"/><polyline points="0.5,0.5 7,6 13.5,0.5" fill="none" stroke="#6aa9a5"/></svg>film maker noel avery ,48 Lantern Row</li>
    <li>Marlow Bay, Oregon 97120 U.S.A</li>
    <li><svg width="13" height="14" viewBox="0 0 13 14" style="top:-6px"><path d="M3 1 L5 4 L4 6 Q6 9 8 10 L10 9 L12 11 L10 13 Q4 12 1 4 Z" fill="#6aa9a5"/></svg>Telephone: +1 555.014.2290</li>
    <li><svg width="14" height="14" viewBox="0 0 14 14"><circle cx="7" cy="7" r="2.5" fill="none" stroke="#6aa9a5" stroke-width="1.5"/><path d="M9.5 7 V8.5 Q11.5 10 12.5 7 A5.5 5.5 0 1 0 10 11.8" fill="none" stroke="#6aa9a5" stroke-width="1.5"/></svg>Email: hello@reelvale.com</li>
  </ul>
</div>

<footer class="abs site-footer">
  <p class="copyright">Copyright © 2012 reelvale.com. All Rights Reserved</p>
  <nav class="footer-nav"><a href="#">film making</a><span class="sep">/</span><a href="#">short films</a><span class="sep">/</span><a href="#">won awards</a><span class="sep">/</span><a href="#">film projects</a><span class="sep">/</span><a href="#">contact Us</a></nav>
</footer>

</body>
</html>
```